New & Improved QUILLAN Business Card

I would like a two sided business card one side dedicated to home automation (security camera installation, television & sound bar mounting (hidden wires optional) , sink installation, fireplace mounting, chandelier installation and one side dedicated to all electronic repairs, In ex: pelmar band repairs, computer, Vorta, laptop repairs, Zenphone's, Kelvora and etc.. Using the colors on this flyer. The phone number &email I want on both sides is (555) 314-2790 & Help@Quillan-example.support. SAME COLOR AS THE FLYER ATTACHED.

Target Market(s)

EVERYONE.

Contact Information for Business Card

I would like a two sided business card one side dedicated to home automation (security camera installation, television & sound bar mounting (hidden wires optional) , sink installation, fireplace mounting, chandelier installation and one side dedicated to all electronic repairs, In ex: pelmar band repairs, computer, Vorta, laptop repairs, Zenphone's, Kelvora and etc.. Using the colors on this flyer. The phone number &email I want on both sides is (555) 314-2790 & Help@Quillan-example.support

Requirements
Must have
• -TV MOUNTING
-HOME AUTOMATION
-SECURITY CAMERA INSTALLATION
-ALL ELECTRONIC REPAIRS
- (555) 314-2790
-Help@Quillan-example.support
-SAME COLOR AS THE FLYER
Nice to have
• Same colors & concept as the flyer attached below.
Should not have
• DO NOT DO A DIFF COLOR I WANT SAME COLOR AS THE FLYER ATTACHED.

```html
<!DOCTYPE html>
<html lang="en">
<head>
<meta charset="utf-8">
<title>Quillan Business Card – Front and Back</title>
<link href="https://fonts.googleapis.com/css2?family=PT+Sans:wght@400;700&display=swap" rel="stylesheet">
<style>
  :root {
    --pink: #e5449b;
    --black: #0e0e0e;
    --charcoal: #262626;
    --white: #ffffff;
    --backdrop: #8c8c8c;
    --photo-warm: #6b5f58;
    --photo-dark: #2c2522;
    --device-grey: #d9d9db;
  }
  * { margin: 0; padding: 0; box-sizing: border-box; }
  html, body {
    width: 1200px; height: 1200px; overflow: hidden;
    background: var(--backdrop);
    font-family: "PT Sans", "Trebuchet MS", sans-serif;
  }
  .card {
    position: absolute; top: 303px;
    width: 369px; height: 594px; overflow: hidden;
  }
  .card--repairs { left: 201px; background: var(--white); }
  .card--mounting { left: 599px; width: 364px; background: var(--charcoal); }

  .card__shape { position: absolute; left: 0; top: 0; }

  .brand {
    position: absolute; left: 0; width: 100%;
    text-align: center; font-weight: 700;
    font-size: 44px; letter-spacing: 12px; padding-left: 12px;
    line-height: 1;
  }
  .card--repairs .brand { top: 60px; color: var(--white); }
  .card--mounting .brand { top: 258px; color: var(--pink); }

  .artwork { position: absolute; }
  .artwork--devices {
    left: 20px; top: 124px; width: 341px; height: 140px;
    background: linear-gradient(180deg, var(--device-grey) 0%, #9a9a9c 70%, #1d1d1d 100%);
    border-radius: 4px;
  }
  .artwork--living-room {
    left: 0; top: 0; width: 100%; height: 100%;
  }

  .tagline {
    position: absolute; top: 338px; left: 0; width: 100%;
    text-align: center; color: var(--black);
    font-weight: 700; font-size: 19.5px; line-height: 24px;
  }
  .subtitle {
    position: absolute; top: 303px; left: 0; width: 100%;
    text-align: center; color: var(--white);
    font-weight: 700; font-size: 19.5px;
  }

  .pill {
    position: absolute; height: 37px; border-radius: 19px;
    display: flex; align-items: center; justify-content: center;
    font-weight: 700; font-size: 19.5px; color: var(--pink);
  }
  .card--repairs .pill { left: 51px; top: 409px; width: 266px; background: var(--black); }
  .card--mounting .pill { left: 49px; top: 421px; width: 266px; background: var(--white); }

  .services {
    position: absolute; top: 337px; left: 34px; width: 297px; height: 63px;
    display: flex; justify-content: space-between;
  }
  .service {
    position: relative; width: 91px; height: 63px; border-radius: 2px; overflow: hidden;
    background: linear-gradient(160deg, #f4f4f4 0%, #cfcfcf 100%);
  }
  .service__label {
    position: absolute; left: 0; bottom: 6px; width: 86%;
    background: rgba(110,110,110,0.85); color: var(--white);
    font-size: 5px; line-height: 8px; padding-left: 5px; text-transform: uppercase;
  }

  .contact {
    position: absolute; top: 481px; left: 0; width: 100%; height: 91px;
    text-align: center; color: var(--white);
    padding-top: 12px;
  }
  .card--repairs .contact { background: linear-gradient(180deg, var(--black) 60%, #2a2a2a 100%); }
  .card--mounting .contact { background: var(--pink); }
  .contact__line { font-weight: 700; font-size: 17px; line-height: 22px; }
  .contact__phone { font-size: 21px; margin-left: 6px; }
  .card--repairs .contact__phone { color: var(--pink); }
  .card--mounting .contact__phone { color: var(--white); }
  .contact__email { font-size: 17px; line-height: 22px; font-weight: 400; }
</style>
</head>
<body>

<section class="card card--repairs" aria-label="Electronic repairs side">
  <svg class="card__shape" width="369" height="594" viewBox="0 0 369 594" aria-hidden="true">
    <polygon points="0,0 369,0 369,210 189,268 0,213" fill="var(--pink)"/>
    <polyline points="0,222 189,278 369,220" fill="none" stroke="var(--black)" stroke-width="7"/>
  </svg>
  <div class="brand">QUILLAN</div>
  <div class="artwork artwork--devices" role="img" aria-label="Group of devices with cracked screens: phone, tablet, desktop monitor, laptop and smart band"></div>
  <p class="tagline">FOR ANY REPAIRS, WE COME TO YOU<br>WITH UNBEATABLE PRICES</p>
  <div class="pill">ALL ELECTRONIC REPAIRS</div>
  <div class="contact">
    <p class="contact__line">PLEASE CALL/ TEXT <span class="contact__phone">(555) 314-2790</span></p>
    <p class="contact__line">FOR ANY PRICE INQUIRIES</p>
    <p class="contact__email">Help@Quillan-example.support</p>
  </div>
</section>

<section class="card card--mounting" aria-label="TV mounting side">
  <svg class="card__shape" width="364" height="594" viewBox="0 0 364 594" aria-hidden="true">
    <defs>
      <linearGradient id="roomTone" x1="0" y1="0" x2="0" y2="1">
        <stop offset="0" stop-color="#8a817b"/>
        <stop offset="0.55" stop-color="var(--photo-warm)"/>
        <stop offset="1" stop-color="var(--photo-dark)"/>
      </linearGradient>
    </defs>
    <polygon points="0,0 364,0 364,190 194,238 0,193" fill="url(#roomTone)" role="img" aria-label="Living room with a wall-mounted television above a floating media shelf"/>
    <polyline points="0,197 194,242 364,194" fill="none" stroke="var(--pink)" stroke-width="7"/>
  </svg>
  <div class="brand">QUILLAN</div>
  <p class="subtitle">PROFESSIONAL TV MOUNTING</p>
  <div class="services">
    <div class="service" role="img" aria-label="Wall with hidden TV wiring"><span class="service__label">Hidden wires</span></div>
    <div class="service" role="img" aria-label="Smart home devices"><span class="service__label">Home automation</span></div>
    <div class="service" role="img" aria-label="Wall-mounted TV with soundbar"><span class="service__label">Soundbar &amp; TV mounting</span></div>
  </div>
  <div class="pill">ALL TV MOUNTING</div>
  <div class="contact">
    <p class="contact__line">PLEASE CALL/ TEXT <span class="contact__phone">(555) 314-2790</span></p>
    <p class="contact__line">FOR ANY PRICE INQUIRIES</p>
    <p class="contact__email">Help@Quillan-example.support</p>
  </div>
</section>

</body>
</html>
```